PawNook business card

Looking for a fun and cool biz card for a new company with patent pending products. I have products to help and protect dogs hearing. My colors are pantone blue and orange.
Updates

Please add tag line: Protect the ones you love...even your PawNooks!

Target Market(s)

Animal/Dog lovers!

Industry/Entity Type

Retail

Contact Information for Business Card

I'm looking for something simple yet fun with all the info included for biz cards

Colors
0555a3
f78f20

Requirements
Must have
• Logo
Nice to have
• name, website and email
Should not have
• phone number

```html
<!DOCTYPE html>
<html lang="en">
<head>
<meta charset="utf-8">
<title>PawNook Business Card</title>
<link href="https://fonts.googleapis.com/css2?family=Open+Sans:wght@400;600;700;800&display=swap" rel="stylesheet">
<style>
  :root {
    --page-bg: #e9e6e3;
    --card-white: #fbfbfb;
    --brand-blue: #0b3089;
    --brand-orange: #f4600f;
    --text-light: #ffffff;
  }
  * { box-sizing: border-box; margin: 0; padding: 0; }
  html, body {
    width: 1200px;
    height: 900px;
    overflow: hidden;
    background: var(--page-bg);
    font-family: "Open Sans", Arial, sans-serif;
  }
  .business-card {
    position: absolute;
    left: 180px;
    top: 190px;
    width: 840px;
    height: 520px;
    background: var(--card-white);
    box-shadow: 0 10px 30px rgba(0,0,0,0.18);
    overflow: hidden;
  }
  .brand-area {
    position: absolute;
    left: 0; top: 0;
    width: 100%;
    height: 280px;
    display: flex;
    flex-direction: column;
    align-items: center;
    justify-content: center;
    gap: 6px;
  }
  .brand-lockup {
    display: flex;
    align-items: center;
    gap: 18px;
  }
  .brand-dot {
    width: 26px;
    height: 26px;
    border-radius: 50%;
    background: var(--brand-orange);
  }
  .brand-name {
    font-size: 82px;
    font-weight: 800;
    line-height: 1.1;
    color: var(--brand-orange);
    letter-spacing: -1px;
  }
  .tagline {
    font-size: 21px;
    font-weight: 600;
    color: var(--brand-blue);
    letter-spacing: 0.2px;
  }
  .accent-rule {
    position: absolute;
    left: 0; top: 280px;
    width: 100%;
    height: 6px;
    background: var(--brand-orange);
  }
  .contact-band {
    position: absolute;
    left: 0; top: 286px;
    width: 100%;
    height: 234px;
    background: var(--brand-blue);
    color: var(--text-light);
  }
  .person {
    position: absolute;
    right: 446px;
    top: 52px;
    text-align: right;
  }
  .person-name {
    font-size: 28px;
    font-weight: 700;
    letter-spacing: 0.3px;
    line-height: 1.2;
  }
  .person-role {
    font-size: 21px;
    font-weight: 400;
    line-height: 1.4;
  }
  .divider {
    position: absolute;
    left: 421px;
    top: 50px;
    width: 2px;
    height: 80px;
    background: var(--text-light);
  }
  .contact-list {
    position: absolute;
    left: 440px;
    top: 59px;
    list-style: none;
  }
  .contact-item {
    display: flex;
    align-items: center;
    gap: 10px;
    font-size: 22px;
    line-height: 31px;
  }
  .contact-icon {
    width: 15px;
    height: 15px;
    flex: none;
  }
  .address {
    position: absolute;
    left: 0;
    top: 156px;
    width: 100%;
    text-align: center;
    padding-left: 70px;
    font-size: 22px;
  }
</style>
</head>
<body>
  <div class="business-card">
    <div class="brand-area">
      <div class="brand-lockup">
        <span class="brand-dot"></span>
        <span class="brand-name">PawNook</span>
      </div>
      <p class="tagline">Protect the ones you love...even your PawNooks!</p>
    </div>
    <div class="accent-rule"></div>
    <div class="contact-band">
      <div class="person">
        <div class="person-name">MARCUS HALE</div>
        <div class="person-role">Managing Director</div>
      </div>
      <div class="divider"></div>
      <ul class="contact-list">
        <li class="contact-item">
          <svg class="contact-icon" viewBox="0 0 24 24" aria-hidden="true"><rect x="2" y="5" width="20" height="14" fill="#ffffff"/><path d="M3 6l9 7 9-7" fill="none" stroke="#0b3089" stroke-width="2"/></svg>
          <span>info@youremail.com</span>
        </li>
        <li class="contact-item">
          <svg class="contact-icon" viewBox="0 0 24 24" aria-hidden="true"><circle cx="12" cy="12" r="10" fill="#ffffff"/><path d="M2 12h20M12 2c3 3 3 17 0 20M12 2c-3 3-3 17 0 20" fill="none" stroke="#0b3089" stroke-width="1.6"/></svg>
          <span>www.websitename.com</span>
        </li>
      </ul>
      <div class="address">1234, Address GoesHere, Country name, 12345</div>
    </div>
  </div>
</body>
</html>
```